Hybrid Repair & Maintenance Services for Molvar & Velno (Need a Postcard Design)

We need a 5 x 7 postcard, to be handed out...Not Mailed. Both sides would have content. We have the least costly options to take care of a Molvar and Velno Hybrid batteries. Also Hybrid Repair & Maintenance Services (the large pack) Please feel free to use whatever you feel would make this pop (if possible) :) I have attached a one page attempt to bring content to you.

Target Market(s)

Molvar and Velno Hybrid Consumers

```html
<!DOCTYPE html>
<html lang="en">
<head>
<meta charset="utf-8">
<title>Keystone Auto – Hybrid Service Postcard</title>
<link rel="stylesheet" href="https://fonts.googleapis.com/css2?family=Libre+Baskerville:wght@400;700&family=Crimson+Text:wght@400;600;700&display=swap">
<style>
  :root {
    --backdrop: #e9e4dc;
    --card-dark: #1e1e1e;
    --red: #e0401b;
    --red-deep: #b8220e;
    --yellow: #f2c40d;
    --yellow-text: #f3c315;
    --white: #ffffff;
    --text-light: #e8e8e8;
    --contact-red: #c8271a;
  }
  * { margin: 0; padding: 0; box-sizing: border-box; }
  html, body { width: 846px; height: 1200px; overflow: hidden; }
  body {
    background: var(--backdrop);
    position: relative;
    font-family: "Crimson Text", Georgia, serif;
    color: var(--text-light);
  }
  .card {
    position: absolute;
    left: 50px;
    width: 742px;
    height: 528px;
    overflow: hidden;
    background: var(--card-dark);
    box-shadow: 0 4px 14px rgba(0,0,0,.35);
  }
  .card--front { top: 57px; }
  .card--back { top: 625px; }

  .card__shapes { position: absolute; inset: 0; width: 742px; height: 528px; }

  /* Front */
  .dash-photo {
    position: absolute; left: 0; top: 0; width: 742px; height: 400px;
    background:
      radial-gradient(circle at 200px 150px, #2f4a78 0, #15233c 90px, #0b0e16 170px, transparent 200px),
      radial-gradient(circle at 620px 260px, #1a1f2b 0, #0c0d10 120px),
      #0a0a0d;
  }
  .brand-title {
    position: absolute; left: 420px; top: 18px; width: 310px;
    font-family: "Libre Baskerville", Georgia, serif;
    font-size: 22px; line-height: 32px; color: var(--white);
    text-transform: uppercase; letter-spacing: .5px; text-align: center;
  }
  .mil-badge {
    position: absolute; left: 590px; top: 143px; width: 120px; height: 120px;
    border-radius: 50%; background: var(--yellow);
    display: flex; align-items: center; justify-content: center; text-align: center;
    font-family: "Libre Baskerville", Georgia, serif; font-weight: 700;
    font-size: 12px; line-height: 17px; color: #3b2a05;
  }
  .tagline-left {
    position: absolute; left: 18px; top: 370px;
    font-family: "Libre Baskerville", Georgia, serif; text-transform: uppercase; color: var(--white);
  }
  .tagline-left__small { font-size: 19px; line-height: 26px; display: block; }
  .tagline-left__mid { font-size: 23px; line-height: 32px; display: block; }
  .tagline-left__big { font-size: 31px; line-height: 38px; display: block; color: var(--red); }
  .warning {
    position: absolute; right: 22px; top: 306px; width: 420px; text-align: right;
    font-family: "Libre Baskerville", Georgia, serif; text-transform: uppercase; color: var(--white);
  }
  .warning__line1 { display: block; font-size: 27px; line-height: 34px; }
  .warning__line2 { display: block; font-size: 31px; line-height: 40px; }
  .warning__line3 { display: block; font-size: 29px; line-height: 38px; color: var(--red); }
  .warning-note {
    position: absolute; left: 372px; top: 426px; width: 360px; text-align: center;
    font-size: 15.5px; line-height: 20px; color: var(--text-light);
  }

  /* Back */
  .offer-title {
    position: absolute; left: 0; top: 14px; width: 742px; text-align: center;
    font-family: "Libre Baskerville", Georgia, serif; text-transform: uppercase;
    font-size: 19px; color: var(--red); letter-spacing: .3px;
  }
  .offer-subtitle {
    position: absolute; left: 0; top: 44px; width: 742px; text-align: center;
    font-weight: 700; font-size: 16px; color: var(--white);
  }
  .intro {
    position: absolute; left: 18px; top: 78px; width: 708px;
    font-size: 14.5px; line-height: 18px; text-align: justify;
  }
  .col-left { position: absolute; left: 18px; top: 150px; width: 380px; }
  .col-right { position: absolute; left: 431px; top: 150px; width: 295px; }
  .section-heading {
    font-family: "Libre Baskerville", Georgia, serif; font-weight: 700;
    font-size: 15px; line-height: 21px; color: var(--yellow-text);
  }
  .section-sub { font-size: 15px; font-weight: 600; color: var(--yellow-text); margin-top: 2px; }
  .service-list { list-style: none; margin-top: 12px; }
  .service-list li {
    position: relative; padding-left: 14px; margin-bottom: 6px;
    font-size: 14.5px; line-height: 18px; text-align: justify;
  }
  .service-list li::before {
    content: ""; position: absolute; left: 1px; top: 6px;
    width: 6px; height: 6px; border-radius: 50%; background: var(--yellow);
  }
  .battery-offer {
    margin-top: 12px; font-family: "Libre Baskerville", Georgia, serif; font-weight: 700;
    font-size: 12.5px; line-height: 19px; color: var(--yellow-text);
  }
  .battery-types { margin-top: 12px; font-weight: 700; font-size: 15px; color: var(--white); }
  .col-right .col-body { margin-top: 16px; font-size: 14.5px; line-height: 18px; text-align: justify; }
  .contact__invite {
    position: absolute; right: 14px; top: 414px; width: 300px; text-align: right;
    font-family: "Libre Baskerville", Georgia, serif; text-transform: uppercase;
    font-size: 12px; line-height: 16px; color: var(--contact-red);
  }
  .contact__address, .contact__phones {
    position: absolute; top: 476px; font-size: 13.5px; line-height: 17px; font-weight: 600; color: #222;
  }
  .contact__address { left: 432px; }
  .contact__phones { left: 618px; }
  .contact__row { display: flex; align-items: center; gap: 5px; }
  .contact__icon { width: 10px; height: 11px; flex: none; }
</style>
</head>
<body>

<section class="card card--front">
  <div class="dash-photo" role="img" aria-label="Close-up photo of a car dashboard speedometer with warning lights lit"></div>
  <svg class="card__shapes" viewBox="0 0 742 528" aria-hidden="true">
    <polygon points="385,0 742,0 742,40 500,125" fill="var(--red)"/>
    <polygon points="440,0 742,0 742,18 520,92" fill="var(--red-deep)" opacity=".55"/>
    <polygon points="0,275 340,385 742,110 742,140 340,410 0,295" fill="var(--red)"/>
    <polygon points="560,235 742,115 742,128 585,228" fill="var(--red-deep)"/>
    <polygon points="0,295 340,410 742,140 742,175 340,440 0,318" fill="var(--yellow)"/>
    <polygon points="0,318 340,440 742,175 742,528 0,528" fill="var(--card-dark)"/>
    <polygon points="0,474 360,505 742,485 742,493 360,513 0,482" fill="var(--white)"/>
    <polygon points="0,484 360,515 742,495 742,528 0,528" fill="var(--red-deep)"/>
  </svg>
  <div class="brand-title">Keystone Auto<br>Mobile Service</div>
  <div class="mil-badge">Malfunction<br>Indicator Lamp<br>(MIL) warnings</div>
  <div class="tagline-left">
    <span class="tagline-left__small">It starts</span>
    <span class="tagline-left__mid">with a</span>
    <span class="tagline-left__big">Diagnostic</span>
  </div>
  <div class="warning">
    <span class="warning__line1">Don't wait</span>
    <span class="warning__line2">until this</span>
    <span class="warning__line3">happens to you!!</span>
  </div>
  <p class="warning-note">These lights have to be taken seriously, they could be telling you that one or more components are failing.</p>
</section>

<section class="card card--back">
  <svg class="card__shapes" viewBox="0 0 742 528" aria-hidden="true">
    <polygon points="245,528 440,360 742,395 742,408 450,376 272,528" fill="var(--red)"/>
    <polygon points="288,528 460,388 742,398 742,528" fill="var(--red-deep)"/>
    <polygon points="312,528 468,398 742,404 742,528" fill="var(--red)"/>
    <polygon points="338,528 480,406 742,410 742,528" fill="var(--white)"/>
  </svg>
  <h1 class="offer-title">Fleet pricing for the single car owner</h1>
  <p class="offer-subtitle">Hybrid Repair &amp; Maintenance Services for Molvar &amp; Velno</p>
  <p class="intro">Underperforming vehicle? To maintain fuel efficiency, your combustion engine, drive motor, generator and Hybrid battery pack must be in balance with each other. If one system is stressed, the other components suffer, possibly causing unrecoverable damage.</p>

  <div class="col-left">
    <h2 class="section-heading">A Complete Hybrid Vehicle and Hybrid Battery Maintenance &amp; Repair</h2>
    <ul class="service-list">
      <li>Complete computer diagnostic test. Cutting-edge technology for fast and accurate diagnosis of issues.</li>
      <li>Electrical systems inspection. To identify abnormalities in systems and connections.</li>
      <li>Wire and cable check. Outside sheath of cables inspected for cuts and tears.</li>
      <li>Complete vehicle inspection. We look at all conventional systems as well as hybrid-specific systems, and let you know what needs attention now, and what may need attention down the road.</li>
    </ul>
    <p class="battery-offer">KEYSTONE AUTO offers a Full Range of<br>Battery Options for your Hybrid Vehicle Needs</p>
    <p class="battery-types">Conditioned – Rebuilt – Remanufactured</p>
  </div>

  <div class="col-right">
    <h2 class="section-heading">2 key indicators your Hybrid Battery Needs Service</h2>
    <p class="section-sub">Loss of Gas Mileage or Lack of Power</p>
    <p class="col-body">Because your HEV's service light will generally not turn on when your battery starts to underperform, it's important that you're aware of your vehicle's gas mileage and performance, therefore showing you if a service is in order.</p>
  </div>

  <p class="contact__invite">We look forward to<br>your call so we can answer<br>any questions you may have</p>
  <div class="contact__address">
    <div class="contact__row">
      <svg class="contact__icon" viewBox="0 0 10 12" aria-hidden="true"><path d="M5 0a4 4 0 0 1 4 4c0 3-4 8-4 8S1 7 1 4a4 4 0 0 1 4-4z" fill="var(--contact-red)"/><circle cx="5" cy="4" r="1.5" fill="#fff"/></svg>
      <span>2280 Harbor Ln Suite 140</span>
    </div>
    <div style="padding-left:15px">Brenton, WA. 98077</div>
  </div>
  <div class="contact__phones">
    <div class="contact__row">
      <svg class="contact__icon" viewBox="0 0 10 11" aria-hidden="true"><path d="M2 0l2 2.5-1.2 1.5c.7 1.5 1.8 2.6 3.2 3.3L7.5 6 10 8l-1.5 2.5C4 10 0 6 0 1.5z" fill="var(--contact-red)"/></svg>
      <span>555-210-4471</span>
    </div>
    <div class="contact__row">
      <svg class="contact__icon" viewBox="0 0 10 11" aria-hidden="true"><path d="M2 0l2 2.5-1.2 1.5c.7 1.5 1.8 2.6 3.2 3.3L7.5 6 10 8l-1.5 2.5C4 10 0 6 0 1.5z" fill="var(--contact-red)"/></svg>
      <span>555-306-9182</span>
    </div>
  </div>
</section>

</body>
</html>
```